New Business Cards for 3 companies - print and digital Needed FAST!

We have rebranded our company into three separate companies.
We need new business cards for 8 employees, three of whom need a business card for each company - total of 12 cards.
PelmaTor is our property development company.
Veld Brokerage & Management handles property management and real estate transactions.
Lark Design Build is our construction company.
Business cards MUST be able to be both printed and function as digital business cards.
No black backgrounds.
Front should be each employee's information and include the logo from their primary company.
Back should include all three logos.
Please see the uploaded spreadsheet for all the information you need for each card. Also uploaded the .png files for each logo as well as the style guide for each logo.

Contact Information for Business Card

See uploaded spreadsheet for information

Font styles to use
Sans Serif
Other font styles liked:
• match style guide if possible

Requirements
Should not have
• No dark backgrounds on the front (on the back OK.) No pictures of employees. Thanks!

```html
<!DOCTYPE html>
<html lang="en">
<head>
<meta charset="utf-8">
<title>PelmaTor Business Card</title>
<link href="https://fonts.googleapis.com/css2?family=Montserrat:wght@400;500;600;700&family=Roboto+Condensed:wght@400&display=swap" rel="stylesheet">
<style>
  :root{
    --stage:#1f1f21;
    --card-white:#ffffff;
    --card-dark:#3a3a3c;
    --pattern:#403f42;
    --green:#6cc24a;
    --ink:#3d3d3f;
    --ink-soft:#555557;
    --white:#ffffff;
  }
  *{box-sizing:border-box;margin:0;padding:0}
  html,body{width:1200px;height:900px;overflow:hidden}
  body{background:var(--stage);font-family:"Montserrat",sans-serif;position:relative}
  .card{position:absolute;left:285px;width:630px;height:360px;overflow:hidden}
  .card-front{top:60px;background:var(--card-white);color:var(--ink)}
  .card-back{top:480px;background:var(--card-dark)}

  /* front */
  .brand{position:absolute;left:44px;top:36px;display:flex;align-items:center;gap:14px}
  .brand-square{width:50px;height:50px;background:var(--green)}
  .brand-name{font-weight:600;font-size:34px;letter-spacing:1px;line-height:1;color:var(--ink)}
  .brand-tag{font-size:10px;letter-spacing:2.4px;font-weight:500;margin-top:6px;padding-top:5px;border-top:1px solid var(--green);color:var(--ink)}
  .accent-bar{position:absolute;left:0;top:146px;width:14px;height:26px;background:var(--green)}

  .info{position:absolute;left:120px;top:116px;display:flex;flex-direction:column;gap:12px;font-size:13px;line-height:1.4;color:var(--ink)}
  .person-name{font-weight:700;font-size:20px;line-height:1.2;color:var(--green);letter-spacing:.3px}
  .person-title{font-size:13px;color:var(--ink-soft)}
  .contacts{list-style:none}
  .contacts li{display:flex;align-items:center;gap:8px}
  .contacts svg{width:11px;height:11px;flex:none}
  .licences{font-size:12.5px}
  .licences b{color:var(--green);font-weight:600}

  /* back */
  .pattern{position:absolute;inset:0;background:var(--pattern);opacity:.5}
  .back-logo{position:absolute;color:var(--white)}
  .back-pelma{left:36px;top:30px;display:flex;align-items:center;gap:12px}
  .back-pelma .brand-name{color:var(--white);font-size:30px}
  .back-pelma .brand-square{width:44px;height:44px}
  .back-pelma .brand-tag{color:var(--white);font-size:9px}
  .back-veld{left:215px;top:130px}
  .back-veld .word{font-weight:700;font-size:52px;letter-spacing:3px;line-height:1;color:var(--white)}
  .back-veld .sub{font-size:10px;letter-spacing:2.6px;margin-top:6px}
  .back-lark{right:48px;bottom:34px;text-align:right}
  .back-lark .word{font-weight:700;font-size:46px;letter-spacing:3px;line-height:1;color:var(--white)}
  .back-lark .sub{font-size:11px;letter-spacing:3px;margin-top:6px}
  .back-lark .motto{font-family:"Roboto Condensed",sans-serif;font-size:11px;color:#cfcfcf;margin-top:3px}
</style>
</head>
<body>

<section class="card card-front" aria-label="Business card front">
  <div class="brand">
    <span class="brand-square"></span>
    <div>
      <div class="brand-name">PelmaTor</div>
      <div class="brand-tag">INVEST. BUILD. MANAGE.</div>
    </div>
  </div>
  <span class="accent-bar"></span>
  <div class="info">
    <div class="person">
      <div class="person-name">DANIEL MAREN</div>
      <div class="person-title">CEO/Owner</div>
    </div>
    <p class="address">48 N. Harlow Ave., Ste 3B,<br>Bramwell IL 60000</p>
    <ul class="contacts">
      <li><svg viewBox="0 0 12 12"><rect x="3" y="0.5" width="6" height="11" rx="1" fill="none" stroke="#6cc24a" stroke-width="1.2"/></svg>555-201-4837</li>
      <li><svg viewBox="0 0 12 12"><path d="M2 1.5h2.5l1 3-1.5 1a6 6 0 0 0 2.5 2.5l1-1.5 3 1V10a1 1 0 0 1-1 1A9 9 0 0 1 1 2.5a1 1 0 0 1 1-1z" fill="#6cc24a"/></svg>555-302-7719 x101</li>
      <li><svg viewBox="0 0 12 12"><rect x="0.5" y="2.5" width="11" height="7" fill="#6cc24a"/><path d="M0.5 2.5 6 7l5.5-4.5" fill="none" stroke="#fff" stroke-width="1"/></svg>dmaren@pelmator.com</li>
      <li><svg viewBox="0 0 12 12"><circle cx="6" cy="6" r="5.5" fill="#6cc24a"/><path d="M0.5 6h11M6 0.5c-3 3-3 8 0 11M6 0.5c3 3 3 8 0 11" fill="none" stroke="#fff" stroke-width=".8"/></svg>www.pelmator.com</li>
    </ul>
    <p class="licences">
      <b>IL RE Lic#:</b> 000.123456 Chicago<br>
      <b>GC Lic#:</b> TGC000000
    </p>
  </div>
</section>

<section class="card card-back" aria-label="Business card back">
  <div class="pattern" role="img" aria-label="Faint repeating monogram pattern across the card"></div>
  <div class="back-logo back-pelma">
    <span class="brand-square"></span>
    <div>
      <div class="brand-name">PelmaTor</div>
      <div class="brand-tag">INVEST. BUILD. MANAGE.</div>
    </div>
  </div>
  <div class="back-logo back-veld">
    <div class="word">VELD</div>
    <div class="sub">BROKERAGE | MANAGEMENT</div>
  </div>
  <div class="back-logo back-lark">
    <div class="word">LARK</div>
    <div class="sub">DESIGN | BUILD</div>
    <div class="motto">Built Right, Built LARK</div>
  </div>
</section>

</body>
</html>
```